Business card design needed for Varrick Medical Practice

We need a new design for our growing medical practice. Our previous design used blue, white and black. I would like to have a design with a baby, child, adult and grandparent on it. We look after a wide range of patients from newborns to 100 year olds.

Industry/Entity Type

Medical

Contact Information for Business Card

Varrick Medical Practice
14 Kestrel Rd Lawson, NSW 2791
Ph 4812 6274 Fax 4831 9527
Dr Maud Pirelli Dr Beatrix Dunmore
Dr Yvonne Kaczmar Dr Estelle Whitcombe
Dr Tom Vasquillo Dr Rex Lund-Patmore
Open Mon- Fri 9-1, 2-5pm
Sat 9-12pm by appointment
web:www.varrickmedical.com.au
email:varrickmedical@quillpost.com

```html
<!DOCTYPE html>
<html lang="en">
<head>
<meta charset="utf-8">
<title>Varrick Medical Practice – Business Card</title>
<link rel="stylesheet" href="https://fonts.googleapis.com/css2?family=Open+Sans:wght@400;700;800&family=Marcellus&display=swap">
<style>
  :root {
    --page: #eef1f3;
    --blue-deep: #2b5c7c;
    --blue-mid: #3a7aa0;
    --blue-light: #5fa6c9;
    --band-light: #ffffff;
    --band-grey: #c9ccce;
    --ink: #2a2a2a;
    --ink-blue: #2f6d93;
    --text-light: #d9ebf4;
  }
  * { box-sizing: border-box; margin: 0; padding: 0; }
  html, body { width: 1200px; height: 1000px; overflow: hidden; }
  body {
    background: var(--page);
    display: flex; align-items: center; justify-content: center;
  }
  .card {
    position: relative;
    width: 1000px; height: 600px;
    overflow: hidden;
    background: radial-gradient(ellipse at 45% 35%, var(--blue-light) 0%, var(--blue-mid) 45%, var(--blue-deep) 100%);
    box-shadow: 0 18px 40px rgba(20, 50, 70, 0.25);
  }
  .hours {
    position: absolute; top: 48px; right: 70px;
    font-family: "Marcellus", serif; font-size: 21px;
    color: var(--text-light); letter-spacing: 0.2px;
  }
  .family-illustration {
    position: absolute; left: 440px; top: 92px;
    width: 400px; height: 238px;
    border-radius: 60px 90px 0 0;
    background: linear-gradient(180deg, #6d94ad 0%, #dfe4e8 75%, #eef0f1 100%);
  }
  .band {
    position: absolute; left: 0; right: 0; top: 330px; height: 175px;
    background: linear-gradient(180deg, var(--band-light) 0%, #e6e7e8 55%, var(--band-grey) 100%);
  }
  .brand {
    position: absolute; left: 80px; top: 148px;
    font-family: "Open Sans", sans-serif; font-weight: 800;
    font-size: 58px; line-height: 1; letter-spacing: -1px;
    color: #ffffff;
  }
  .address {
    position: absolute; left: 80px; top: 352px;
    font-family: "Open Sans", sans-serif; font-style: normal;
    font-size: 19px; line-height: 1.3;
    color: var(--ink);
  }
  .address .street {
    display: flex; align-items: center; gap: 8px;
    font-size: 24px; color: var(--ink-blue); margin-bottom: 2px;
  }
  .address .street-no {
    display: inline-flex; align-items: center; justify-content: center;
    width: 30px; height: 30px; border: 2px solid var(--ink-blue); border-radius: 50%;
    font-size: 15px;
  }
  .address .line { display: block; padding-left: 16px; }
  .doctors {
    position: absolute; left: 385px; top: 352px;
    display: grid; grid-template-columns: 255px 290px; row-gap: 10px;
    list-style: none;
    font-family: "Open Sans", sans-serif; font-size: 21px; color: var(--ink);
  }
  .doctors li::before { content: "•"; margin-right: 10px; }
  .contact-strip {
    position: absolute; left: 0; right: 0; top: 505px; bottom: 0;
    display: flex; align-items: center; justify-content: space-around;
    padding: 0 60px;
    font-family: "Marcellus", serif; font-size: 22px; color: var(--text-light);
  }
</style>
</head>
<body>
  <main class="card">
    <p class="hours">Open Mon-Fri 9-1, 2-5pm Sat 9-12pm by appointment</p>

    <div class="family-illustration" role="img" aria-label="Silhouettes of a grandparent, an adult, a child and a baby representing patients of all ages"></div>

    <div class="band"></div>

    <h1 class="brand">Varrick<br>Medical<br>Practice</h1>

    <address class="address">
      <span class="street">Kestrel Rd Brindlewood <span class="street-no">14</span></span>
      <span class="line">NSW 2791</span>
      <span class="line">Ph 4812 6274</span>
      <span class="line">Fax 4831 9527</span>
    </address>

    <ul class="doctors">
      <li>Dr Maud Pirelli</li>
      <li>Dr Beatrix Dunmore,</li>
      <li>Dr Yvonne Kaczmar</li>
      <li>Dr Estelle Whitcombe,</li>
      <li>Dr Tom Vasquillo</li>
      <li>Dr Rex Lund-Patmore</li>
    </ul>

    <footer class="contact-strip">
      <span class="web">web: www.varrickmedical.com.au</span>
      <span class="email">email: varrickmedical@quillpost.com</span>
    </footer>
  </main>
</body>
</html>
```